P.K.Harbor Services Business Card

We need a bi-lingual card (spanish/english). Information should be name, hours, services and address/phone. I am including a flyer as a reference--much of the information is included on it (spanish/english as well). THE COMPANY IS CALLED "P.K. HARBOR SERVICES" AND WE THINK THAT "P.K." SHOULD SUFFICE AS A LOGO--BUT WE DON'T HAVE THAT FONT NAILED DOWN. Colors should be Green/Blue scale. Happy colors. It's a check cashing business.

```html
<!DOCTYPE html>
<html lang="en">
<head>
<meta charset="utf-8">
<title>P.K. Harbor Services – Business Card</title>
<link rel="stylesheet" href="https://fonts.googleapis.com/css2?family=Oswald:wght@700&family=Arimo:wght@400;700&family=Pinyon+Script&display=swap">
<style>
  :root {
    --backdrop: #1d1d1d;
    --card-white: #f4f4f4;
    --card-black: #0c0c0c;
    --green: #8ab83a;
    --green-edge: #5f9bd1;
    --ink: #1a1a1a;
    --rule: #8c8c8c;
    --white: #ffffff;
  }
  * { box-sizing: border-box; margin: 0; padding: 0; }
  html, body {
    width: 1200px; height: 900px; overflow: hidden;
    background: var(--backdrop);
  }
  .stage {
    position: relative; width: 1200px; height: 900px;
    display: flex; align-items: center; justify-content: center; gap: 40px;
  }
  .card {
    position: relative; width: 540px; height: 309px;
    box-shadow: 0 10px 30px rgba(0,0,0,.6);
    overflow: hidden;
  }

  /* Front */
  .card--front { background: var(--card-white); color: var(--ink); }
  .headline {
    position: absolute; left: 40px; top: 20px; width: 340px;
    border-top: 1px solid var(--rule); border-bottom: 1px solid var(--rule);
    padding: 4px 0 3px; text-align: center; white-space: nowrap;
  }
  .headline__title {
    font-family: "Oswald", sans-serif; font-weight: 700;
    font-size: 46px; line-height: 1.05; letter-spacing: -.5px;
    color: var(--green); -webkit-text-stroke: .8px var(--green-edge);
  }
  .tagline {
    position: absolute; left: 40px; top: 86px; width: 340px;
    font-family: "Pinyon Script", cursive; font-size: 22px; line-height: 1.1;
    text-align: center; white-space: nowrap;
  }
  .address {
    position: absolute; right: 26px; top: 140px;
    font-family: "Arimo", sans-serif; font-size: 14px; line-height: 1.25;
    text-transform: uppercase; letter-spacing: .5px;
  }
  .contact {
    position: absolute; left: 30px; top: 158px;
    font-family: "Arimo", sans-serif; text-transform: uppercase;
  }
  .contact__phone { font-size: 26px; letter-spacing: .5px; line-height: 1.05; }
  .contact__hours { font-size: 13px; letter-spacing: .4px; margin-top: 2px; }
  .partners {
    position: absolute; left: 30px; right: 20px; top: 224px;
    display: flex; gap: 22px; align-items: center; list-style: none;
    font-family: "Arimo", sans-serif; font-weight: 700; font-size: 11px;
    text-transform: uppercase; color: var(--ink);
  }
  .partner { display: flex; align-items: center; gap: 6px; }
  .partner__mark { width: 12px; height: 12px; background: var(--ink); }
  .partner__mark--round { border-radius: 50%; }
  .band {
    position: absolute; left: 0; right: 0; bottom: 0; height: 40px;
    background: var(--card-black); color: var(--white);
    font-family: "Arimo", sans-serif; font-size: 14px; letter-spacing: .8px;
    text-transform: uppercase; text-align: center; line-height: 40px;
  }

  /* Back */
  .card--back { background: var(--card-black); color: var(--white); }
  .brand {
    position: absolute; left: 0; right: 0; top: 78px;
    display: flex; align-items: center; justify-content: center; gap: 12px;
  }
  .brand__square { width: 22px; height: 22px; background: var(--green); }
  .brand__name {
    font-family: "Arimo", sans-serif; font-weight: 700;
    font-size: 30px; letter-spacing: 1.5px; color: var(--green);
    text-transform: uppercase; line-height: 1.1;
  }
  .spanish {
    position: absolute; left: 0; right: 0; top: 180px; text-align: center;
    font-family: "Pinyon Script", cursive; font-size: 32px;
  }
</style>
</head>
<body>
<main class="stage">
  <section class="card card--front" aria-label="Card front">
    <div class="headline"><h1 class="headline__title">CHECK CA$HING</h1></div>
    <p class="tagline">All Checks Welcome! Best Rates<br>in Maple County</p>
    <p class="address">48 Lantern Road<br>Maple Ridge, NY</p>
    <div class="contact">
      <p class="contact__phone">(555) 014 - 2280</p>
      <p class="contact__hours">Monday-Saturday (9AM-9PM)</p>
    </div>
    <ul class="partners" role="list">
      <li class="partner"><span class="partner__mark"></span>Meridian Transfer</li>
      <li class="partner"><span class="partner__mark"></span>QuickBill Pay</li>
      <li class="partner"><span class="partner__mark partner__mark--round"></span>Orbis Card</li>
    </ul>
    <p class="band">Business and Contractor's Checks Welcomed!</p>
  </section>

  <section class="card card--back" aria-label="Card back">
    <div class="brand">
      <span class="brand__square"></span>
      <p class="brand__name">P.K. Harbor Services</p>
    </div>
    <p class="spanish" lang="es">Se Habla Español</p>
  </section>
</main>
</body>
</html>
```